bramblewood mental health web page

this is to be a single page with no links - will function just like an add.
will have 2 biographies
contact info.
Updates

Dear Designers - most of these are too complex.

 Just want one page with contact details (yet to be sorted). No email contact as we can't monitor all emails and if person emails saying suicidal I am potentially accountable if they are successful. Hence- this is just like a listing in a phone book. 
2 photos - one of me the other my husband - with a little blurb next to our names.
No info on fees or appointments etc
I am legally not allowed use language like - "what sets us apart" - it suggests we are better than other clinicians and that is illegal. 
NO EMOTIVE PHOTOS PLEASE! 

Target Market(s)

clients wanting check background and contact information.

Industry/Entity Type

Mental Health

Requirements
Must have
• NEW LOGO
space for photographs
Old web page to complicated
http://wbtk.net.au/index.shtml
Should not have
• anything that flashes.

```html
<!DOCTYPE html>
<html lang="en">
<head>
<meta charset="utf-8">
<title>Bramblewood Mental Health — Maren &amp; Tobias Ashcombe</title>
<link href="https://fonts.googleapis.com/css2?family=Alegreya+Sans:wght@400;500;700;800&display=swap" rel="stylesheet">
<style>
  :root {
    --bg-top: #2f6f62;
    --bg-mid: #6fa88f;
    --bg-low: #a9c3a0;
    --bg-bottom: #d8d3a4;
    --panel: rgba(42, 52, 44, 0.82);
    --panel-edge: rgba(255, 255, 255, 0.06);
    --text-light: #f1f3ee;
    --text-soft: #e8eee9;
    --rule: rgba(255, 255, 255, 0.55);
    --accent-ring: #1a8fc0;
    --logo-ink: #1d4e63;
    --footer-ink: #5f6a5a;
    --icon: #d8e0e4;
  }
  * { box-sizing: border-box; margin: 0; padding: 0; }
  html, body { width: 1200px; height: 1060px; overflow: hidden; }
  body {
    font-family: "Alegreya Sans", sans-serif;
    color: var(--text-light);
    background:
      radial-gradient(ellipse 420px 160px at 180px 60px, rgba(20,70,60,.55), transparent 70%),
      radial-gradient(ellipse 300px 200px at 1100px 60px, rgba(20,70,60,.6), transparent 70%),
      radial-gradient(ellipse 520px 140px at 260px 260px, rgba(20,80,68,.45), transparent 70%),
      linear-gradient(180deg, var(--bg-top) 0%, var(--bg-mid) 30%, var(--bg-low) 60%, var(--bg-bottom) 100%);
    position: relative;
    letter-spacing: .07em;
  }
  .brand {
    position: absolute; left: 498px; top: 26px; width: 204px; height: 82px;
    background: #fff; border-radius: 8px;
    box-shadow: 0 3px 8px rgba(0,0,0,.3);
    display: flex; align-items: center; justify-content: center; gap: 10px;
  }
  .brand-mark { width: 16px; height: 16px; background: var(--logo-ink); }
  .brand-name {
    font-size: 17px; font-weight: 700; color: var(--logo-ink);
    line-height: 1.05; text-transform: uppercase; letter-spacing: .03em;
  }
  .top-rule {
    position: absolute; left: 116px; top: 137px; width: 968px; height: 3px;
    border-top: 1px solid rgba(255,255,255,.35); border-bottom: 1px solid rgba(255,255,255,.25);
  }
  .bios {
    position: absolute; left: 143px; top: 176px; width: 918px;
    display: flex; justify-content: space-between;
  }
  .bio { width: 452px; text-align: center; }
  .portrait {
    width: 200px; height: 200px; margin: 0 auto;
    border-radius: 50%; border: 3px solid var(--accent-ring);
    background: radial-gradient(circle at 50% 40%, #f4f4f4 0%, #cfcfcf 55%, #7a7a7a 100%);
    box-shadow: 0 3px 10px rgba(0,0,0,.35);
  }
  .name {
    margin-top: 14px; font-size: 38px; line-height: 44px;
    font-weight: 700; letter-spacing: .05em;
    text-shadow: 0 2px 3px rgba(0,0,0,.25);
  }
  .credentials {
    margin-top: 9px; font-size: 13px; line-height: 20px;
    color: var(--text-soft); letter-spacing: .1em;
  }
  .services {
    position: absolute; left: 143px; top: 537px; width: 918px;
    display: flex; gap: 13px;
  }
  .service-card {
    width: 220px; height: 276px; background: var(--panel);
    border: 1px solid var(--panel-edge); border-radius: 6px;
    padding: 20px 14px 0 18px; font-size: 13.5px; line-height: 19px;
  }
  .card-title {
    font-size: 14.5px; line-height: 17px; font-weight: 500; padding-bottom: 8px;
    border-bottom: 1px dotted var(--rule); margin-bottom: 12px;
  }
  .card-title.compact { font-size: 13.5px; }
  .card-title.narrow { padding-right: 48px; }
  .item-list { list-style: none; }
  .item-list li { padding-left: 14px; position: relative; }
  .item-list li::before {
    content: ""; position: absolute; left: 1px; top: 6px;
    width: 7px; height: 8px; border: 1px solid var(--text-light);
  }
  .item-list li.sub { padding-left: 18px; }
  .item-list li.sub::before {
    width: 6px; height: 6px; border-radius: 50%; top: 7px; left: 5px;
  }
  .focus-row { display: flex; align-items: center; gap: 15px; margin: 6px 0 18px 2px; }
  .focus-thumb { width: 46px; height: 45px; border-radius: 3px; }
  .thumb-low { background: linear-gradient(135deg, #2a2030, #6b4a58); }
  .thumb-tense { background: linear-gradient(135deg, #e6d4c0, #a27a5e); }
  .contact-bar {
    position: absolute; left: 144px; top: 824px; width: 916px; height: 110px;
    background: var(--panel); border-radius: 4px;
    font-size: 13px; line-height: 20px;
  }
  .contact { position: absolute; top: 30px; display: flex; gap: 8px; }
  .contact svg { flex: none; margin-top: 3px; }
  .contact b { font-weight: 700; }
  .copyright {
    position: absolute; top: 1030px; left: 0; width: 1200px; text-align: center;
    font-size: 13px; color: var(--footer-ink); letter-spacing: .1em;
  }
</style>
</head>
<body>
  <header class="brand">
    <span class="brand-mark"></span>
    <span class="brand-name">Bramblewood<br>Mental Health</span>
  </header>
  <div class="top-rule"></div>

  <section class="bios">
    <article class="bio">
      <div class="portrait" role="img" aria-label="Portrait photo of Maren Ashcombe"></div>
      <h1 class="name">Maren Ashcombe</h1>
      <p class="credentials">
        M. Psych (Clinical), M. Genetic Couns., B.A. (Psych),<br>
        Reg. no: PSY0000418237 Provider no: 5803926T<br>
        Member of the Australasian Guild of Psychology
      </p>
    </article>
    <article class="bio">
      <div class="portrait" role="img" aria-label="Portrait photo of Tobias Ashcombe"></div>
      <h1 class="name">Tobias Ashcombe</h1>
      <p class="credentials">
        M. Psych (Counselling), B.Soc.Sc. (Hons),<br>
        Reg. no: PSY0000562914 Provider no: 3917408J<br>
        Member of the Australasian Guild of Psychology
      </p>
    </article>
  </section>

  <section class="services">
    <article class="service-card">
      <h2 class="card-title">Specialising in the treatment of:</h2>
      <div class="focus-row"><div class="focus-thumb thumb-low" role="img" aria-label="Small photo for depression"></div><span>Depression</span></div>
      <div class="focus-row"><div class="focus-thumb thumb-tense" role="img" aria-label="Small photo for anxiety"></div><span>Anxiety</span></div>
    </article>
    <article class="service-card">
      <h2 class="card-title compact">Provider of psychological assessment and therapy for other mental healt prob-lems including:</h2>
      <ul class="item-list">
        <li>Phobias</li><li>Panic</li><li>Adjustment disorder</li><li>Bereavement</li>
        <li>Post-traumatic stress dis-order</li><li>Eating disorders</li><li>Obsessive Compulsive dis-</li>
      </ul>
    </article>
    <article class="service-card">
      <h2 class="card-title narrow">Counselling and therapy provided for:</h2>
      <ul class="item-list">
        <li>Families</li><li>Couples (Partner Bridge Program)</li><li>Group</li><li>Individuals</li>
        <li class="sub">Children</li><li class="sub">Adolescents</li><li class="sub">Adults</li><li class="sub">Older persons</li>
      </ul>
    </article>
    <article class="service-card">
      <h2 class="card-title">Other Services:</h2>
      <ul class="item-list">
        <li>Cognitive Assessment</li><li>Neuropsychological Assessment</li>
        <li>Memory &amp; Dementia Screening</li><li>Employee Assistance Program</li>
        <li>Stress Management</li><li>Medicolegal reports</li>
      </ul>
    </article>
  </section>

  <footer class="contact-bar">
    <div class="contact" style="left:90px">
      <svg width="16" height="16" viewBox="0 0 16 16"><path d="M8 1 L15 8 H13 V15 H3 V8 H1 Z" fill="var(--icon)"/></svg>
      <p><b>Address:</b> 27 Larkfield<br>Place, HOLLOWAY 6031</p>
    </div>
    <div class="contact" style="left:378px">
      <svg width="18" height="18" viewBox="0 0 18 18"><path d="M4 1 L7 5 L5 7 C6 10 8 12 11 13 L13 11 L17 14 L15 17 C8 16 2 10 1 3 Z" fill="var(--icon)"/></svg>
      <p><b>Phone:</b> (08)9510-3864<br>04-3816-2207</p>
    </div>
    <div class="contact" style="left:665px">
      <p><b>ABN:</b> 48 206 915 372<br><b>ACN:</b> 274819305</p>
    </div>
  </footer>

  <p class="copyright">© Copyright 2013. All rights reserved.</p>
</body>
</html>
```